Baby acupressure app for parents

We need an app for parents that teaches parents how to help them relieve their baby's imbalances (stomach ache, trouble sleeping etc.)

Please see the attached document (with info) and wireframes.

This project is urgent so please only participate if you're able to finish all screens within a few days after the contest is over.

Target Market(s)

Baby moms (20-40 years of age)

Industry/Entity Type

Baby Care

Colors
886aae
b768aa
e667a6
f68d4d
faa54b
fac994
f9ba93
f59195
fee18a

Requirements
Must have
• A high quality design that is both modern and very sleek and stylish.
Nice to have
• Simple animations to make the app "feel" like it's extreme high quality and make the user want to use it again and again
Should not have
• Sandwich menus

```html
<!DOCTYPE html>
<html lang="en">
<head>
<meta charset="utf-8">
<title>Tendra – Welcome</title>
<link rel="stylesheet" href="https://fonts.googleapis.com/css2?family=Quicksand:wght@400;600;700&display=swap">
<style>
  :root {
    --overlay-deep: #8f6f9f;
    --overlay-mid: #a17fae;
    --overlay-light: #b896bd;
    --overlay-warm: #c39ab8;
    --text-white: #ffffff;
  }
  * { margin: 0; padding: 0; box-sizing: border-box; }
  html, body {
    width: 675px;
    height: 1200px;
    overflow: hidden;
  }
  body {
    font-family: "Quicksand", sans-serif;
    color: var(--text-white);
    background: var(--overlay-mid);
  }
  .welcome-screen {
    position: relative;
    width: 675px;
    height: 1200px;
    overflow: hidden;
  }
  .hero-photo {
    position: absolute;
    inset: 0;
    background:
      radial-gradient(ellipse 55% 40% at 50% 55%, var(--overlay-warm) 0%, rgba(195,154,184,0) 70%),
      radial-gradient(ellipse 40% 25% at 35% 28%, var(--overlay-light) 0%, rgba(184,150,189,0) 75%),
      linear-gradient(180deg, var(--overlay-mid) 0%, var(--overlay-deep) 100%);
  }
  .headline {
    position: absolute;
    left: 232px;
    top: 154px;
    line-height: 1.2;
  }
  .headline-light {
    display: block;
    font-size: 35px;
    font-weight: 400;
    letter-spacing: 0.3px;
  }
  .headline-bold {
    display: block;
    font-size: 30px;
    font-weight: 700;
    letter-spacing: 0.2px;
  }
  .brand {
    position: absolute;
    left: 0;
    right: 0;
    top: 770px;
    display: flex;
    align-items: center;
    justify-content: center;
    gap: 14px;
  }
  .brand-dot {
    width: 22px;
    height: 22px;
    border-radius: 50%;
    background: var(--text-white);
  }
  .brand-name {
    font-size: 44px;
    font-weight: 600;
    letter-spacing: 1px;
    color: var(--text-white);
  }
  .begin-button {
    position: absolute;
    left: 213px;
    top: 939px;
    width: 250px;
    height: 69px;
    border: 2px solid var(--text-white);
    border-radius: 9px;
    background: transparent;
    color: var(--text-white);
    font-family: "Quicksand", sans-serif;
    font-size: 28px;
    font-weight: 600;
    letter-spacing: 3px;
    display: flex;
    align-items: center;
    justify-content: center;
  }
</style>
</head>
<body>
  <main class="welcome-screen">
    <div class="hero-photo" role="img" aria-label="Photo of a smiling mother holding her baby on her lap, tinted with a soft purple overlay"></div>

    <h1 class="headline">
      <span class="headline-light">Help relieve</span>
      <span class="headline-bold">your child’s imbalances</span>
    </h1>

    <div class="brand">
      <span class="brand-dot"></span>
      <span class="brand-name">Tendra</span>
    </div>

    <button class="begin-button" type="button">Begin</button>
  </main>
</body>
</html>
```